Tellwick Asset Management - Corporate Letter Head Project

Looking for a classy design based on our current logo. Please find current logo source file in files. With our color scheme.

Target Market(s)

We're an investment firm, the letterhead needs to look professional and attractive to clients.

Industry/Entity Type

Hedgefund

Colors
0054AA
0677BA
7BADD7
CADEEF
E8F1F8

Requirements
Must have
• Our logo, address, phone number, and email

```html
<!DOCTYPE html>
<html lang="en">
<head>
<meta charset="utf-8">
<title>Tellwick Asset Management – Letterhead</title>
<link href="https://fonts.googleapis.com/css2?family=Open+Sans:wght@400;600;700&display=swap" rel="stylesheet">
<style>
  :root {
    --navy: #012a5c;
    --ink: #1d1d1f;
    --body: #6b6b6b;
    --muted: #5c5c5c;
    --rule: #d4d6db;
    --grey-1: #f1f2f4;
    --grey-2: #e7e8eb;
    --grey-3: #dcdee1;
    --backdrop: #ebecef;
    --paper: #ffffff;
  }
  * { margin: 0; padding: 0; box-sizing: border-box; }
  html, body { width: 922px; height: 1200px; overflow: hidden; }
  body {
    background: var(--backdrop);
    font-family: "Open Sans", Arial, sans-serif;
    position: relative;
  }
  .letterhead {
    position: absolute;
    left: 154px; top: 170px;
    width: 613px; height: 859px;
    background: var(--paper);
    overflow: hidden;
  }
  .header-trim, .footer-trim { position: absolute; left: 0; }
  .header-trim { top: 0; }
  .footer-trim { top: 800px; }

  .brand {
    position: absolute; left: 55px; top: 168px;
    color: var(--navy); font-weight: 600;
    font-size: 17px; line-height: 20px; letter-spacing: 0.3px;
  }

  .company-contact {
    position: absolute; right: 59px; top: 113px;
    list-style: none; text-align: right;
    font-size: 9.5px; color: var(--muted); line-height: 13px;
  }
  .company-contact li {
    display: flex; justify-content: flex-end; align-items: flex-start; gap: 5px;
  }
  .company-contact li + li { margin-top: 7px; }
  .company-contact .icon {
    width: 13px; height: 13px; flex: none;
    background: var(--navy); border-radius: 2px;
  }

  .recipient { position: absolute; left: 56px; top: 270px; }
  .recipient-name { color: var(--navy); font-size: 15px; font-weight: 700; line-height: 20px; }
  .recipient-role { font-size: 8px; color: var(--ink); margin-bottom: 4px; }
  .recipient-details { list-style: none; font-size: 10px; color: var(--ink); line-height: 16.5px; }
  .recipient-details b { color: var(--navy); display: inline-block; width: 20px; }

  .date {
    position: absolute; right: 60px; top: 334px;
    font-size: 10.5px; color: var(--ink);
  }

  .letter-body {
    position: absolute; left: 56px; top: 387px; width: 497px;
    font-size: 10px; line-height: 21.5px; color: var(--body);
    white-space: nowrap; overflow: hidden;
  }
  .letter-body p + p { margin-top: 21.5px; }

  .sign-off { position: absolute; left: 420px; top: 672px; width: 124px; text-align: center; }
  .signature { display: block; margin: 0 auto 2px; }
  .signer-name { font-size: 10px; font-weight: 700; color: var(--ink); line-height: 12px; }
  .signer-role { font-size: 10px; color: var(--ink); line-height: 12px; }
</style>
</head>
<body>
  <main class="letterhead">
    <svg class="header-trim" width="613" height="30" viewBox="0 0 613 30" aria-hidden="true">
      <rect x="0" y="0" width="613" height="4" fill="var(--navy)"/>
      <rect x="105" y="6" width="508" height="9" fill="var(--rule)"/>
      <polygon points="0,0 112,0 94,28 0,28" fill="var(--navy)"/>
    </svg>

    <div class="brand">TELLWICK ASSET<br>MANAGEMENT</div>

    <ul class="company-contact">
      <li><span>2715 Larchmont Avenue<br>Arlington, VA 22201</span>
        <svg class="icon" viewBox="0 0 13 13" aria-hidden="true"><rect width="13" height="13" rx="2" fill="var(--navy)"/><path d="M6.5 2.3a2.6 2.6 0 0 0-2.6 2.6c0 2 2.6 5.6 2.6 5.6s2.6-3.6 2.6-5.6a2.6 2.6 0 0 0-2.6-2.6zm0 3.6a1 1 0 1 1 0-2 1 1 0 0 1 0 2z" fill="#fff"/></svg></li>
      <li><span>+01 703 555 0142</span>
        <svg class="icon" viewBox="0 0 13 13" aria-hidden="true"><rect width="13" height="13" rx="2" fill="var(--navy)"/><path d="M4 2.8l1.4 1.6-.7 1.2a5 5 0 0 0 2.7 2.7l1.2-.7 1.6 1.4-.8 1.3C6.3 10.1 2.9 6.7 2.7 3.6z" fill="#fff"/></svg></li>
      <li><span>office@tellwickam.com</span>
        <svg class="icon" viewBox="0 0 13 13" aria-hidden="true"><rect width="13" height="13" rx="2" fill="var(--navy)"/><rect x="2.5" y="3.8" width="8" height="5.6" fill="none" stroke="#fff" stroke-width="1"/><path d="M2.6 3.9l3.9 3 3.9-3" fill="none" stroke="#fff" stroke-width="1"/></svg></li>
      <li><span>www.tellwickam.com</span>
        <svg class="icon" viewBox="0 0 13 13" aria-hidden="true"><rect width="13" height="13" rx="2" fill="var(--navy)"/><path d="M4.3 2.8v7l1.8-1.6 1.2 2.6 1.1-.5-1.2-2.5 2.3-.2z" fill="#fff"/></svg></li>
    </ul>

    <section class="recipient">
      <div class="recipient-name">Marren Hale</div>
      <div class="recipient-role">Chief Director</div>
      <ul class="recipient-details">
        <li><b>A :</b>18-3, Keppel Lane Singapore - 0712</li>
        <li><b>W :</b>m.hale@halemail.com, www.halecapital.com</li>
        <li><b>P :</b>+65 - 61234 - 5078</li>
      </ul>
    </section>

    <div class="date">Date, 10 September, 2019</div>

    <article class="letter-body">
      <p>This is a sample letter that has been placed to demonstrate typing remat (Your Company). letterhead<br>
      design. When positioned properly, it will serve to work in harmony with all other elements letterhead.<br>
      This letterhead design is meant to project an image</p>
      <p>This letterhead design is meant project an image of professionalism reliability. By using simple aligen<br>
      we have created a very spacious feeling. The simplicity suggest&nbsp; rengththe spaciousnes contributes h<br>
      aesthetics the layout. These basic qualities along with the (Your Company)</p>
      <p>look and helps reinforce the (Your Company) brand. letterhead design is meant to project an image p<br>
      design. When positioned properly, it will serve to work in harmony all the other elements letterhead.<br>
      sionalism and reliability.</p>
    </article>

    <div class="sign-off">
      <svg class="signature" width="108" height="30" viewBox="0 0 108 30" role="img" aria-label="Handwritten signature of Priya Castell">
        <rect width="108" height="30" rx="3" fill="var(--grey-1)"/>
      </svg>
      <div class="signer-name">Priya Castell</div>
      <div class="signer-role">Manager</div>
    </div>

    <svg class="footer-trim" width="613" height="59" viewBox="0 0 613 59" aria-hidden="true">
      <rect x="15" y="14" width="253" height="2" fill="var(--rule)"/>
      <polygon points="288,5 352,5 340,25 280,25" fill="var(--grey-1)"/>
      <polygon points="352,5 416,5 404,25 340,25" fill="var(--grey-2)"/>
      <polygon points="416,5 476,5 464,25 404,25" fill="var(--grey-3)"/>
      <polygon points="490,4 613,4 613,59 0,59 0,30 473,30" fill="var(--navy)"/>
    </svg>
  </main>
</body>
</html>
```